Marigolds a fast food restaurant need a flag designed, has the images uploaded

I have the logo and images, need images to be resized and text added under the images.
This is a two sided flag and to be printed with flagmintpress.com,
I need the flag to have the logo on one side and the food images on the other side with identifier underneath it
like
Paratha Wrap
Rice Bowl
Vellori
Naan Pizza

The images might need some modifications and resizing. I will also need to be placed to make the biggest impact on the design

Target Market(s)

Street sign

Industry/Entity Type

Fast Food Restaurant

Font styles to use
Sans Serif

Colors

Designer to choose colors to be used in the design.

Requirements
Must have
• It must have clarity and sharpness
Nice to have
• border highlight and make any changes that could make it better. I ma open to suggestions.
Should not have
• misalignment. smudges, pixelisation

```html
<!DOCTYPE html>
<html lang="en">
<head>
<meta charset="utf-8">
<title>Marigolds – Feather Flags</title>
<link rel="stylesheet" href="https://fonts.googleapis.com/css2?family=Josefin+Sans:wght@300;400&family=Lobster&family=Montserrat:wght@500&display=swap">
<style>
  :root {
    --canvas: #ffffff;
    --flag-yellow: #f6bb22;
    --flag-yellow-deep: #f0a81c;
    --ring-orange: #f39a1d;
    --sleeve: #141414;
    --pole: #f2f2f2;
    --pole-edge: #c9c9c9;
    --brand-red: #b8401e;
    --label-fill: #fbe96a;
    --label-edge: #3a2a05;
    --ink: #3b2a10;
  }
  html, body {
    margin: 0;
    padding: 0;
    width: 1200px;
    height: 1198px;
    overflow: hidden;
    background: var(--canvas);
  }
  .flag-set { display: block; width: 1200px; height: 1198px; }
  .flag-body { fill: var(--flag-yellow); }
  .flag-sleeve { fill: var(--sleeve); }
  .pole { fill: var(--pole); stroke: var(--pole-edge); stroke-width: 1; }
  .ground-spike { fill: none; stroke: var(--pole-edge); stroke-width: 3; }
  .food-ring { fill: var(--ring-orange); }
  .food-label {
    font-family: "Lobster", cursive;
    font-size: 30px;
    fill: var(--label-fill);
    stroke: var(--label-edge);
    stroke-width: 1.2px;
    paint-order: stroke;
  }
  .brand-name {
    font-family: "Josefin Sans", sans-serif;
    font-weight: 400;
    fill: var(--brand-red);
  }
  .brand-tagline {
    font-family: "Josefin Sans", sans-serif;
    font-weight: 300;
    fill: var(--brand-red);
    letter-spacing: 1px;
  }
  .brand-dot { fill: var(--brand-red); }
  .web-address {
    font-family: "Montserrat", sans-serif;
    font-weight: 500;
    fill: var(--ink);
  }
</style>
</head>
<body>
<svg class="flag-set" viewBox="0 0 1200 1198" xmlns="http://www.w3.org/2000/svg">
  <defs>
    <linearGradient id="wrap-tone" x1="0" y1="0" x2="1" y2="1">
      <stop offset="0" stop-color="#e8c99a"/><stop offset="1" stop-color="#b9824a"/>
    </linearGradient>
    <linearGradient id="bowl-tone" x1="0" y1="0" x2="0" y2="1">
      <stop offset="0" stop-color="#e9efe0"/><stop offset="1" stop-color="#a8431f"/>
    </linearGradient>
    <linearGradient id="panini-tone" x1="0" y1="0" x2="1" y2="1">
      <stop offset="0" stop-color="#d9a36a"/><stop offset="1" stop-color="#7d9a4a"/>
    </linearGradient>
    <linearGradient id="pizza-tone" x1="0" y1="0" x2="1" y2="1">
      <stop offset="0" stop-color="#f0d7a8"/><stop offset="1" stop-color="#b5542a"/>
    </linearGradient>
  </defs>

  <!-- Menu flag -->
  <g class="flag flag-menu">
    <rect class="pole" x="166" y="770" width="9" height="320"/>
    <path class="ground-spike" d="M167,1045 v52 h20 v-52"/>
    <path class="flag-body" d="M170,262 C176,150 280,86 392,76 C386,300 376,560 352,700 C336,758 262,778 172,778 Z"/>
    <path class="flag-sleeve" d="M166,262 C172,150 276,86 392,74 L392,80 C282,92 180,154 175,262 L175,778 L166,778 Z"/>

    <circle class="food-ring" cx="268" cy="190" r="56"/>
    <circle role="img" aria-label="Photo of a paratha wrap" cx="268" cy="186" r="46" fill="url(#wrap-tone)"/>
    <text class="food-label" x="212" y="226">Paratha</text>
    <text class="food-label" x="240" y="256">Wrap</text>

    <circle class="food-ring" cx="268" cy="350" r="56"/>
    <circle role="img" aria-label="Photo of a rice bowl with curry" cx="268" cy="342" r="46" fill="url(#bowl-tone)"/>
    <text class="food-label" x="208" y="402">Rice Bowl</text>

    <circle class="food-ring" cx="268" cy="488" r="56"/>
    <circle role="img" aria-label="Photo of a grilled panini sandwich" cx="266" cy="484" r="46" fill="url(#panini-tone)"/>
    <text class="food-label" x="206" y="540">Vellori</text>

    <circle class="food-ring" cx="272" cy="632" r="54"/>
    <circle role="img" aria-label="Photo of a naan pizza" cx="272" cy="630" r="46" fill="url(#pizza-tone)"/>
    <text class="food-label" x="206" y="676">Naan</text>
    <text class="food-label" x="234" y="710">Pizza</text>
  </g>

  <!-- Large logo flag -->
  <g class="flag flag-logo-large">
    <rect class="pole" x="433" y="915" width="8" height="175"/>
    <path class="ground-spike" d="M434,1048 v48 h22 v-48"/>
    <path class="flag-body" d="M438,418 C444,340 520,280 612,266 C614,480 614,680 600,780 C580,880 520,916 440,918 Z"/>
    <path class="flag-sleeve" d="M433,418 C440,338 516,278 612,264 L612,270 C524,284 448,342 442,418 L442,918 L433,918 Z"/>
    <g transform="translate(530,600) rotate(-90)">
      <text class="brand-name" x="0" y="0" font-size="40">Marigolds</text>
      <text class="brand-tagline" x="0" y="22" font-size="13">savor the flavor</text>
    </g>
    <circle class="brand-dot" cx="524" cy="704" r="56"/>
    <text class="web-address" x="476" y="799" font-size="9.5">www.marigoldseats.com</text>
  </g>

  <!-- Small logo flag -->
  <g class="flag flag-logo-small">
    <rect class="pole" x="674" y="915" width="8" height="175"/>
    <path class="ground-spike" d="M675,1055 v46 h20 v-46"/>
    <path class="flag-body" d="M680,562 C686,510 740,470 814,458 C815,600 815,720 806,800 C796,880 760,916 682,920 Z"/>
    <path class="flag-sleeve" d="M674,562 C680,508 736,468 814,456 L814,462 C744,474 690,512 684,562 L684,920 L674,920 Z"/>
    <g transform="translate(752,658) rotate(-90)">
      <text class="brand-name" x="0" y="0" font-size="32">Marigolds</text>
      <text class="brand-tagline" x="0" y="18" font-size="10.5">savor the flavor</text>
    </g>
    <circle class="brand-dot" cx="746" cy="736" r="44"/>
    <text class="web-address" x="710" y="820" font-size="7.5">www.marigoldseats.com</text>
  </g>
</svg>
</body>
</html>
```